Property Auctions with Teodor Bramwick

Podcast cover art 3000px by 3000px. Eye catching for a weekly podcast. The words should read Property Auctions (large font) with Teodor Bramwick (smaller font)

I would like the font and colours to be similar to my book, a copy of which I have attached.

Target Market(s)

New and experienced property investors looking to purchase at a property auction

```html
<!DOCTYPE html>
<html lang="en">
<head>
<meta charset="utf-8">
<title>Property Auctions with Teodor Bramwick</title>
<link href="https://fonts.googleapis.com/css2?family=Anton&family=Barlow:wght@500;600&family=Great+Vibes&display=swap" rel="stylesheet">
<style>
  :root {
    --slate: #444f54;
    --scene-light: #6c777b;
    --scene-mid: #586266;
    --gold-light: #f0bf58;
    --gold-deep: #e99f27;
    --gold-name: #e8b84a;
    --white: #ffffff;
  }
  html, body {
    margin: 0;
    padding: 0;
    width: 1200px;
    height: 1200px;
    overflow: hidden;
    background: var(--white);
  }
  .cover {
    position: relative;
    width: 1200px;
    height: 1200px;
    background: var(--slate);
    overflow: hidden;
  }
  .house-scene {
    position: absolute;
    left: 0;
    top: 430px;
    width: 720px;
    height: 770px;
    background: radial-gradient(ellipse at 40% 45%, var(--scene-light) 0%, var(--scene-mid) 45%, var(--slate) 90%);
  }
  .host-portrait {
    position: absolute;
    left: 0;
    top: 0;
    width: 1200px;
    height: 1200px;
  }
  .tagline {
    position: absolute;
    left: 0;
    top: 123px;
    width: 960px;
    margin: 0;
    text-align: center;
    font-family: "Barlow", sans-serif;
    font-weight: 600;
    font-size: 30px;
    line-height: 37px;
    letter-spacing: 0.36em;
    color: var(--white);
  }
  .title {
    position: absolute;
    left: 67px;
    top: 203px;
    margin: 0;
    font-family: "Anton", sans-serif;
    font-weight: 400;
    font-size: 185px;
    line-height: 172px;
    transform: scaleX(1.17);
    transform-origin: left top;
    background: linear-gradient(180deg, var(--gold-deep) 0%, var(--gold-light) 30%, var(--gold-light) 60%, var(--gold-deep) 100%);
    background-size: 100% 172px;
    -webkit-background-clip: text;
    background-clip: text;
    color: transparent;
    white-space: nowrap;
  }
  .subtitle {
    position: absolute;
    left: 69px;
    top: 561px;
    margin: 0;
    font-family: "Barlow", sans-serif;
    font-weight: 500;
    font-size: 40px;
    line-height: 49px;
    letter-spacing: 0.15em;
    color: var(--white);
  }
  .with {
    position: absolute;
    left: 256px;
    top: 990px;
    font-family: "Great Vibes", cursive;
    font-size: 78px;
    line-height: 1;
    color: var(--white);
  }
  .host-name {
    position: absolute;
    left: 71px;
    top: 1068px;
    margin: 0;
    font-family: "Barlow", sans-serif;
    font-weight: 500;
    font-size: 52px;
    line-height: 1;
    letter-spacing: 0.12em;
    color: var(--gold-name);
  }
</style>
</head>
<body>
  <main class="cover">
    <div class="house-scene" role="img" aria-label="Greyscale photo of a suburban house with a sold sign in front"></div>
    <svg class="host-portrait" viewBox="0 0 1200 1200" role="img" aria-label="Portrait of the host in a pinstripe suit and white shirt">
      <defs>
        <linearGradient id="portrait-tone" x1="0" y1="0" x2="0" y2="1">
          <stop offset="0" stop-color="#6e625c"/>
          <stop offset="0.2" stop-color="#b98d7c"/>
          <stop offset="0.42" stop-color="#c99a88"/>
          <stop offset="0.5" stop-color="#e9e9ec"/>
          <stop offset="0.62" stop-color="#3a3a44"/>
          <stop offset="1" stop-color="#1f1f26"/>
        </linearGradient>
      </defs>
      <path d="M850 230 Q850 15 1015 15 Q1185 15 1185 230 L1180 460 Q1200 520 1200 560 L1200 1200 L612 1200 L628 720 Q660 620 760 590 L880 540 Q850 450 850 230 Z" fill="url(#portrait-tone)"/>
    </svg>

    <p class="tagline">THE EXPERT'S GUIDE TO SUCCESS<br>IN ALL MARKET CONDITIONS</p>
    <h1 class="title">PROPERTY<br>AUCTIONS</h1>
    <p class="subtitle">REPOSSESSIONS,<br>BANKRUPTCIES AND<br>BARGAIN PROPERTIES</p>
    <span class="with">With</span>
    <p class="host-name">TEODOR BRAMWICK</p>
  </main>
</body>
</html>
```